Book Cover "Venice"

Creation of a cover (14 x 20.5 cm + bleed area) for a book:
Image: “BrumeVerte” (Tiff joined)
AUTHOR: Corinne Valmer
TITLE: The murmurs of Lorient
PUBLISHER: Editions Pluvane (AT THE BOTTOM OF THE COVER)

Target Market(s)

Readers of romantic novels

Industry/Entity Type

Book

```html
<!DOCTYPE html>
<html lang="en">
<head>
<meta charset="utf-8">
<title>The murmurs of Lorient — Corinne Valmer</title>
<link rel="stylesheet" href="https://fonts.googleapis.com/css2?family=Bodoni+Moda:wght@500;600&family=Open+Sans:ital,wght@0,400;1,600&display=swap">
<style>
  :root {
    --frame-red: #d0201c;
    --sky-deep: #4a0707;
    --sky-mid: #b3150f;
    --sky-bright: #e2301c;
    --sky-glow: #f0522a;
    --silhouette: #0d0303;
    --author-red: #f04a36;
    --title-ink: #1c0504;
    --publisher-red: #e0362a;
  }
  * { margin: 0; padding: 0; box-sizing: border-box; }
  html, body {
    width: 831px;
    height: 1200px;
    overflow: hidden;
    background: #ffffff;
  }
  .cover {
    position: relative;
    width: 831px;
    height: 1200px;
    background: var(--frame-red);
    padding: 16px;
  }
  .cover-artwork {
    position: absolute;
    inset: 16px;
    background:
      radial-gradient(ellipse 70% 30% at 60% 55%, rgba(240, 82, 42, 0.55), transparent 70%),
      linear-gradient(180deg,
        var(--sky-deep) 0%,
        var(--sky-mid) 22%,
        var(--sky-bright) 45%,
        var(--sky-glow) 60%,
        var(--sky-mid) 72%,
        #3a0504 82%,
        var(--silhouette) 92%,
        var(--silhouette) 100%);
  }
  .author {
    position: absolute;
    top: 38px;
    left: 0;
    right: 0;
    text-align: center;
    font-family: "Open Sans", sans-serif;
    font-weight: 400;
    font-size: 27px;
    letter-spacing: 0.12em;
    color: var(--author-red);
    text-transform: uppercase;
  }
  .title {
    position: absolute;
    top: 320px;
    left: 0;
    right: 0;
    text-align: center;
    font-family: "Bodoni Moda", serif;
    font-weight: 600;
    color: var(--title-ink);
    text-transform: uppercase;
    line-height: 0.92;
  }
  .title-line { display: block; }
  .title-small { font-size: 84px; }
  .title-mid { font-size: 104px; letter-spacing: 0.01em; }
  .title-large { font-size: 150px; letter-spacing: 0.01em; }
  .publisher {
    position: absolute;
    top: 1030px;
    left: 0;
    right: 40px;
    text-align: center;
    font-family: "Open Sans", sans-serif;
    font-style: italic;
    font-weight: 600;
    font-size: 35px;
    letter-spacing: 0.02em;
    color: var(--publisher-red);
    text-transform: uppercase;
  }
</style>
</head>
<body>
  <main class="cover">
    <div class="cover-artwork" role="img" aria-label="Photograph of a blazing red sunset sky over the dark silhouette of a harbour town with domes and a lit street lamp"></div>
    <p class="author">Corinne Valmer</p>
    <h1 class="title">
      <span class="title-line title-small">The</span>
      <span class="title-line title-mid">Murmurs</span>
      <span class="title-line title-small">of</span>
      <span class="title-line title-large">Lorient</span>
    </h1>
    <p class="publisher">Editions Pluvane</p>
  </main>
</body>
</html>
```